Business Card Design

I would like a new business card design for an accounting firm that specializes in resolving clients tax problems. I want the card to give the impression that we are not your typical stodgy accounting firm, but at the same time we will get the job done.
Industry/Entity Type
Business
Contact Information for Business Card
Dorian T Welsby
Certified Public Accountant
38-27 52nd Street
Sunnyside, NY 11287
Tel: (718) 555-0142
Fax: (888) 555-0199
e-mail: dtwthecpa@ledgerpost.com
website: harborfilingreliefexperts.com

```html
<!DOCTYPE html>
<html lang="en">
<head>
<meta charset="utf-8">
<title>Dorian T. Welsby – Business Card</title>
<link rel="stylesheet" href="https://fonts.googleapis.com/css2?family=Tenor+Sans&family=Didact+Gothic&display=swap">
<style>
  :root {
    --brand-green: #176b47;
    --name-green: #1b6a45;
    --ink: #1c1f1e;
    --panel-grey: rgba(200, 204, 202, 0.85);
    --panel-green: rgba(168, 206, 160, 0.9);
    --white: #ffffff;
    --photo-light: #f3f4f4;
    --photo-mid: #e3e5e6;
    --photo-key: #cdeec0;
  }
  html, body {
    margin: 0;
    padding: 0;
    width: 1200px;
    height: 702px;
    overflow: hidden;
    background: var(--white);
  }
  .card {
    position: relative;
    width: 1200px;
    height: 702px;
    overflow: hidden;
    background: var(--white);
  }
  .keyboard-photo {
    position: absolute;
    left: 78px;
    top: 0;
    width: 1122px;
    height: 480px;
    background:
      radial-gradient(ellipse 180px 200px at 340px 330px, var(--photo-key) 0%, rgba(205,238,192,0.4) 60%, rgba(205,238,192,0) 100%),
      linear-gradient(160deg, var(--photo-light) 0%, var(--photo-mid) 55%, var(--photo-light) 100%);
  }
  .card-shapes {
    position: absolute;
    left: 0;
    top: 0;
  }
  .name-block {
    position: absolute;
    left: 543px;
    top: 223px;
    width: 657px;
    height: 127px;
  }
  .name-block__bar {
    position: absolute;
    left: 0;
    top: 0;
    width: 18px;
    height: 127px;
    background: var(--ink);
  }
  .name-block__panel {
    position: absolute;
    left: 24px;
    top: 1px;
    right: 0;
    height: 125px;
    background: linear-gradient(90deg, var(--panel-green) 0%, var(--panel-grey) 55%, var(--panel-grey) 100%);
  }
  .name-block__name {
    position: absolute;
    left: 60px;
    top: 8px;
    margin: 0;
    font-family: "Tenor Sans", sans-serif;
    font-weight: 400;
    font-size: 56px;
    letter-spacing: 1px;
    color: var(--name-green);
    white-space: nowrap;
  }
  .name-block__title {
    position: absolute;
    left: 116px;
    top: 76px;
    margin: 0;
    font-family: "Tenor Sans", sans-serif;
    font-size: 30px;
    font-variant: small-caps;
    letter-spacing: 0.5px;
    color: var(--ink);
    white-space: nowrap;
  }
  .contact {
    position: absolute;
    left: 70px;
    top: 480px;
    color: var(--white);
    font-family: "Didact Gothic", sans-serif;
  }
  .contact__heading {
    margin: 0 0 8px;
    font-family: Arial, Helvetica, sans-serif;
    font-size: 22px;
    font-weight: 400;
    letter-spacing: 0.5px;
  }
  .contact__list {
    margin: 0;
    padding: 0;
    list-style: none;
    font-size: 21px;
    line-height: 32px;
    letter-spacing: 0.3px;
  }
  .website {
    position: absolute;
    right: 68px;
    top: 646px;
    margin: 0;
    color: var(--white);
    font-family: "Didact Gothic", sans-serif;
    font-size: 21px;
    letter-spacing: 0.4px;
    white-space: nowrap;
  }
</style>
</head>
<body>
<main class="card">
  <div class="keyboard-photo" role="img" aria-label="Close-up photo of a white computer keyboard with a green key marked with a dollar sign"></div>

  <svg class="card-shapes" width="1200" height="702" viewBox="0 0 1200 702" aria-hidden="true">
    <path class="white-sweep" d="M0,372 Q330,445 830,442 Q1050,440 1200,395 L1200,410 Q600,545 0,405 Z" fill="#ffffff"/>
    <path class="green-base" d="M0,402 Q600,545 1200,400 L1200,702 L0,702 Z" fill="#176b47"/>
    <path class="black-swoosh" d="M0,374 Q360,448 830,442 Q380,464 0,396 Z" fill="#1c1f1e"/>
  </svg>

  <header class="name-block">
    <div class="name-block__bar"></div>
    <div class="name-block__panel"></div>
    <h1 class="name-block__name">DORIAN T. WELSBY</h1>
    <p class="name-block__title">Certified public accountant</p>
  </header>

  <section class="contact">
    <h2 class="contact__heading">CONTACT :</h2>
    <ul class="contact__list">
      <li>38-27 52nd Street</li>
      <li>Sunnyside, NY 11287</li>
      <li>Tel: (718) 555-0142</li>
      <li>Fax: (888) 555-0199</li>
      <li>e-mail: dtwthecpa@ledgerpost.com</li>
    </ul>
  </section>

  <p class="website">website: harborfilingreliefexperts.com</p>
</main>
</body>
</html>
```